Professional Personal Website with Blog and four sections

I am seeking a website design for myself. I would like the site to contain a blog, related to Information Security and several sections.

I am an established Information Security Consultant (one aspect of the site).
I am an author of a children's spiritual book that is "new thought" (another aspect of the site)
I am a co-founder of a secure social platform for kids and families (www.tovarelo.net)
I may want a section on finance as well, not sure at this moment

I want this site to be a personal website, not a subscription service or professional services sales site, I want the site to look very professional, so that I can share it with all types of people without concern - business, spiritual, other.

I have provided a photo of myself for the site, smart casual on a beach. The site will be hosted on brennmorlock.net

You can see samples of what I am referring to by searching "personal website" on images.zumvaro.net

I would like the page layout, and the images chopped up as individual jpgs, including hover images for buttons. I can do the coding

I would like the following buttons
Home, About, Information Security Blog, Passion Projects, Contact

I would like the top portion of the page to say "Dorian Pell"
I would like the subtext to say:
Executive Information Security Architect, Author, and Idea Man

I envision the following

Target Market(s)

Executive / Technical / Creative types / Spritual types

Number of Pages Required

4 page

Requirements
Must have
• Blog section
Should not have
• No Matrix themes or No Cop themes, No Fingerprints or Eyeball scans

```html
<!DOCTYPE html>
<html lang="en">
<head>
<meta charset="utf-8">
<title>Dorian Pell</title>
<link rel="stylesheet" href="https://fonts.googleapis.com/css2?family=Open+Sans:wght@400;600;700;800&display=swap">
<style>
:root{
  --blue:#2b8fd3;
  --blue-dark:#1f74ae;
  --ink:#333b44;
  --muted:#8a939c;
  --line:#e3e7ea;
  --bg:#ffffff;
  --soft:#f4f6f8;
  --footer:#1e2c3c;
  --footer-deep:#17232f;
  --footer-text:#aeb9c4;
}
*{box-sizing:border-box;margin:0;padding:0}
html,body{width:1200px;height:2260px;overflow:hidden}
body{background:var(--bg);font-family:"Open Sans",Arial,sans-serif;color:var(--ink);position:relative}
.abs{position:absolute}
a{color:inherit;text-decoration:none}

/* header */
.site-header{left:0;top:0;width:1200px;height:72px}
.brand{left:108px;top:18px;font-size:30px;font-weight:400;color:#1c2630;letter-spacing:-.5px}
.follow{left:740px;top:24px;display:flex;align-items:center;gap:6px;font-size:12px;color:var(--muted)}
.follow .sq{width:22px;height:22px;background:var(--blue);display:inline-block}
.follow .sq.alt{background:#e5603b}
.follow .sq.dk{background:#4a5866}
.search-top{left:900px;top:20px;width:200px;height:32px;background:#2c3845;color:#9aa6b2;font-size:12px;padding:8px 12px}
.main-nav{left:0;top:72px;width:1200px;height:30px;background:var(--blue)}
.main-nav ul{list-style:none;display:flex;margin-left:108px;height:30px;align-items:center}
.main-nav li{color:#fff;font-size:11px;font-weight:700;padding:0 22px 0 0;letter-spacing:.3px}
.main-nav li.active{background:var(--blue-dark);padding:8px 14px;margin-right:14px}

/* hero */
.hero{left:108px;top:112px;width:644px;height:400px;background:linear-gradient(120deg,#d9dde0 0%,#9aa2a8 45%,#5c646b 100%)}
.hero-copy{left:32px;top:110px;color:#fff}
.hero-copy h1{font-size:42px;font-weight:700;line-height:1;text-shadow:0 0 0 transparent}
.hero-copy p{font-size:13px;margin-top:10px;line-height:1.4;width:220px}
.btn{display:inline-block;background:var(--blue);color:#fff;font-size:10px;font-weight:700;padding:7px 14px;letter-spacing:.5px}
.hero-copy .btn{margin-top:14px}
.dots{left:0;bottom:14px;width:644px;display:flex;justify-content:center;gap:6px}
.dots i{width:8px;height:8px;border-radius:50%;background:#fff;opacity:.6;display:block}
.dots i.on{opacity:1;background:var(--blue)}

.side-news{left:768px;top:112px;width:332px;height:400px}
.side-item{height:100px;border-bottom:1px solid var(--line);display:flex;gap:12px;padding:8px 0}
.side-item .thumb{width:84px;height:82px;flex:none}
.side-item .date{font-size:10px;color:var(--muted)}
.side-item h4{font-size:12px;color:var(--blue);font-weight:600;margin:2px 0 4px}
.side-item p{font-size:10px;color:var(--muted);line-height:1.4}

/* feature cards */
.card{top:524px;height:206px;color:#fff}
.card .card-in{position:absolute;left:20px;bottom:20px}
.card h3{font-size:22px;font-weight:700;line-height:1.1;margin-bottom:10px}
.card-sec{left:108px;width:312px;background:linear-gradient(135deg,#b9c2c9,#5d6870)}
.card-thought{left:428px;width:324px;background:linear-gradient(135deg,#2a2620,#6b5318 60%,#e1b23c)}
.card-social{left:768px;width:332px;background:linear-gradient(135deg,#48305c,#b84f7c 55%,#f0a45b)}
.card-finance{left:768px;top:740px;width:332px;height:260px;background:linear-gradient(135deg,#c9cdd0,#8d969c 60%,#5f676d)}

/* posts */
.section-title{font-size:15px;font-weight:800;color:var(--blue);letter-spacing:.3px}
.latest-title{left:108px;top:744px}
.title-rule{left:108px;top:768px;width:644px;height:1px;background:var(--line)}
.post{left:108px;width:644px;height:232px;display:flex;gap:18px}
.post .post-img{width:272px;height:232px;flex:none}
.post .date{font-size:10px;color:var(--muted);margin-top:4px}
.post h2{font-size:14px;font-weight:700;color:var(--blue);line-height:1.35;margin:4px 0 10px}
.post p{font-size:11px;color:var(--muted);line-height:1.6}
.post .more{display:block;font-size:10px;font-weight:700;color:var(--ink);margin-top:12px}
.pager{left:580px;top:1784px;display:flex;gap:4px}
.pager span{width:22px;height:22px;border:1px solid var(--line);font-size:10px;display:flex;align-items:center;justify-content:center;color:var(--ink)}
.pager span.on{background:var(--blue);color:#fff;border-color:var(--blue)}

/* sidebar */
.email-title{left:768px;top:1016px}
.email-text{left:768px;top:1044px;width:332px;font-size:11px;color:var(--muted);line-height:1.6}
.email-form{left:768px;top:1090px;width:332px;height:36px;display:flex}
.email-form .field{flex:1;border:1px solid var(--line);font-size:11px;color:var(--muted);padding:10px 12px}
.email-form .go{width:40px;background:var(--blue);display:flex;align-items:center;justify-content:center}
.box{left:768px;width:332px;border:1px solid var(--line)}
.box-head{height:40px;display:flex;align-items:center;justify-content:space-between;padding:0 14px;border-bottom:1px solid var(--line)}
.box-head .arrows{color:var(--muted);font-size:12px;letter-spacing:6px}
.popular{top:1150px;height:282px}
.pop-item{display:flex;gap:12px;padding:10px 14px;height:60px}
.pop-item .pthumb{width:52px;height:42px;flex:none}
.pop-item h5{font-size:11px;color:var(--blue);font-weight:600}
.pop-item p{font-size:9px;color:var(--muted);line-height:1.4;margin-top:2px}
.links{top:1452px;height:276px}
.links ul{list-style:none;padding:6px 14px}
.links li{font-size:11px;color:var(--ink);padding:8px 0;border-bottom:1px dashed var(--line)}
.links li::before{content:"›";color:var(--blue);font-weight:700;margin-right:8px}

/* footer */
.site-footer{left:0;top:1830px;width:1200px;height:430px;background:var(--footer)}
.foot-col{top:40px;color:var(--footer-text);font-size:11px}
.foot-col h6{color:#fff;font-size:12px;font-weight:700;margin-bottom:14px;letter-spacing:.3px}
.foot-col li{list-style:none;line-height:2}
.foot-col .ico{display:inline-block;width:12px;height:12px;background:var(--blue);margin-right:8px;vertical-align:-2px}
.foot-search{left:900px;top:72px;width:200px;height:30px;background:#2a3b4d;color:#8797a6;font-size:11px;padding:8px 10px}
.foot-bottom{left:0;top:340px;width:1200px;height:90px;background:var(--footer-deep)}
.foot-bottom p{position:absolute;left:108px;top:16px;font-size:10px;color:var(--footer-text)}
</style>
</head>
<body>

<header class="abs site-header">
  <div class="abs brand">Dorianpell</div>
  <div class="abs follow">Follow us on <span class="sq"></span><span class="sq"></span><span class="sq alt"></span><span class="sq dk"></span></div>
  <div class="abs search-top">Search</div>
</header>
<nav class="abs main-nav">
  <ul>
    <li class="active">HOME</li><li>ABOUT US</li><li>SERVICES</li><li>INFORMATIONS</li><li>NEWS</li><li>FEATURES</li><li>GALLERY</li><li>CONTACT US</li>
  </ul>
</nav>

<section class="abs hero" role="img" aria-label="Close-up photo of padlocks on a chain">
  <div class="abs hero-copy">
    <h1>information<br>security</h1>
    <p>Contrary to popular belief, lorem ipsum is not simply.</p>
    <span class="btn">READ MORE</span>
  </div>
  <div class="abs dots"><i class="on"></i><i></i><i></i><i></i></div>
</section>

<aside class="abs side-news">
  <div class="side-item"><div class="thumb" role="img" aria-label="Keyboard photo" style="background:linear-gradient(135deg,#4a5a6a,#9aa8b4)"></div><div><div class="date">Jan 08, 2015</div><h4>The greatest lands of career</h4><p>Contrary to popular belief lorem is not simply random text.</p></div></div>
  <div class="side-item"><div class="thumb" role="img" aria-label="Laptop photo" style="background:linear-gradient(135deg,#5e6f80,#c5ced6)"></div><div><div class="date">Jan 08, 2015</div><h4>There are many variations</h4><p>Contrary to popular belief lorem is not simply random text.</p></div></div>
  <div class="side-item"><div class="thumb" role="img" aria-label="Network cables photo" style="background:linear-gradient(135deg,#22466a,#4f86b8)"></div><div><div class="date">Jan 08, 2015</div><h4>Many desktop publishing</h4><p>Contrary to popular belief lorem is not simply random text.</p></div></div>
  <div class="side-item" style="border-bottom:0"><div class="thumb" role="img" aria-label="Office desk photo" style="background:linear-gradient(135deg,#6f7a84,#b6bec5)"></div><div><div class="date">Jan 08, 2015</div><h4>It is a long established fact</h4><p>Contrary to popular belief lorem is not simply random text.</p></div></div>
</aside>

<div class="abs card card-sec" role="img" aria-label="Padlock photo for the security consulting section"><div class="card-in"><h3>Information<br>Security<br>Consultant</h3><span class="btn">READ MORE</span></div></div>
<div class="abs card card-thought" role="img" aria-label="Glowing light bulb photo for the book section"><div class="card-in"><h3>New<br>Thought</h3><span class="btn">READ MORE</span></div></div>
<div class="abs card card-social" role="img" aria-label="Colourful social network photo for the platform section"><div class="card-in"><h3>Secure Social<br>Platform</h3><span class="btn">READ MORE</span></div></div>
<div class="abs card card-finance" role="img" aria-label="Stacked coins photo for the finance section"><div class="card-in"><h3>Finance</h3><p style="font-size:11px;margin-bottom:10px">Contrary to popular belief, lorem ipsum.</p><span class="btn">READ MORE</span></div></div>

<h2 class="abs section-title latest-title">LATEST POSTS</h2>
<div class="abs title-rule"></div>

<article class="abs post" style="top:784px">
  <div class="post-img" role="img" aria-label="Hands typing on a laptop keyboard" style="background:linear-gradient(135deg,#27496b,#6b9bc3)"></div>
  <div><div class="date">September 08, 2015</div><h2>But I must explain to you how all this mistaken idea of denouncing pleasure</h2><p>Sed ut perspiciatis unde omnis iste natus error sit voluptatem accusantium doloremque laudantium, totam rem aperiam, eaque ipsa quae ab illo inventore veritatis et quasi architecto beatae vitae dicta.</p><span class="more">READ MORE »</span></div>
</article>
<article class="abs post" style="top:1032px">
  <div class="post-img" role="img" aria-label="Blue digital world map graphic" style="background:linear-gradient(135deg,#0f3b6e,#3d8fd1)"></div>
  <div><div class="date">September 08, 2015</div><h2>At vero eos et accusamus et iusto odio dignissimos ducimus qui blanditiis praesentium</h2><p>Nemo enim ipsam voluptatem quia voluptas sit aspernatur aut odit aut fugit, sed quia consequuntur magni dolores eos qui ratione voluptatem sequi nesciunt neque porro quisquam.</p><span class="more">READ MORE »</span></div>
</article>
<article class="abs post" style="top:1280px">
  <div class="post-img" role="img" aria-label="Security shield on a circuit background" style="background:linear-gradient(135deg,#123457,#3f6f9c)"></div>
  <div><div class="date">September 08, 2015</div><h2>On the other hand, we denounce with righteous indignation and dislike men</h2><p>Who are so beguiled and demoralized by the charms of pleasure of the moment, so blinded by desire, that they cannot foresee the pain and trouble that are bound to ensue daily.</p><span class="more">READ MORE »</span></div>
</article>
<article class="abs post" style="top:1528px">
  <div class="post-img" role="img" aria-label="Figure holding an umbrella in the rain" style="background:linear-gradient(135deg,#2b2f36,#7a838c)"></div>
  <div><div class="date">September 08, 2015</div><h2>Temporibus autem quibusdam et aut officiis debitis aut rerum necessitatibus</h2><p>Saepe eveniet ut et voluptates repudiandae sint et molestiae non recusandae. Itaque earum rerum hic tenetur a sapiente delectus, ut aut reiciendis voluptatibus maiores alias.</p><span class="more">READ MORE »</span></div>
</article>
<div class="abs pager"><span>‹</span><span class="on">1</span><span>2</span><span>3</span><span>4</span><span>5</span><span>›</span></div>

<h2 class="abs section-title email-title">GET EMAIL UPDATES</h2>
<p class="abs email-text">Contrary to popular belief, lorem ipsum is not simply random text. Sign up today.</p>
<div class="abs email-form"><div class="field">Email Address</div><div class="go"><svg width="12" height="12" viewBox="0 0 12 12"><path d="M4 2l4 4-4 4" stroke="#fff" stroke-width="2" fill="none"/></svg></div></div>

<aside class="abs box popular">
  <div class="box-head"><span class="section-title">POPULAR POSTS</span><span class="arrows">‹ ›</span></div>
  <div class="pop-item"><div class="pthumb" role="img" aria-label="Padlock thumbnail" style="background:#9aa3aa"></div><div><h5>Temporibus autem</h5><p>Sed ut perspiciatis unde omnis by Dorian Pell</p></div></div>
  <div class="pop-item"><div class="pthumb" role="img" aria-label="Laptop thumbnail" style="background:#3f6f9c"></div><div><h5>But I must explain to you</h5><p>Sed ut perspiciatis unde omnis by Dorian Pell</p></div></div>
  <div class="pop-item"><div class="pthumb" role="img" aria-label="Network thumbnail" style="background:#1f4f80"></div><div><h5>At vero eos et accusamus</h5><p>Sed ut perspiciatis unde omnis by Dorian Pell</p></div></div>
  <div class="pop-item"><div class="pthumb" role="img" aria-label="Rain thumbnail" style="background:#555d66"></div><div><h5>To take a trivial example</h5><p>Sed ut perspiciatis unde omnis by Dorian Pell</p></div></div>
</aside>

<aside class="abs box links">
  <div class="box-head"><span class="section-title">USEFUL LINKS</span></div>
  <ul>
    <li>Lorem ipsum dolor sit amet</li>
    <li>On the other hand, we denounce</li>
    <li>But I must explain to you</li>
    <li>Temporibus autem quibusdam</li>
    <li>To take a trivial example</li>
    <li>Who are so beguiled and</li>
    <li>When our power of choice</li>
  </ul>
</aside>

<footer class="abs site-footer">
  <div class="abs foot-col" style="left:108px"><h6>MORE INFORMATION</h6><ul><li>HOME</li><li>ABOUT US</li><li>SERVICES</li><li>FEATURES</li><li>NEWS</li><li>GALLERY</li><li>CONTACT US</li></ul></div>
  <div class="abs foot-col" style="left:330px"><h6>LINKS</h6><ul><li>TERMS AND CONDITIONS</li><li>PRIVACY POLICY</li><li>FAQ</li><li>BLOG</li></ul></div>
  <div class="abs foot-col" style="left:560px"><h6>CONTACT US</h6><ul><li>4127 Harlow Avenue, Brenton</li><li>MA 02184</li><li>+1 (555) 014-2290</li><li>hello@brennmorlock.net</li></ul></div>
  <div class="abs foot-col" style="left:760px"><h6>FOLLOW US ON</h6><ul><li><span class="ico"></span>Social page</li><li><span class="ico"></span>Short posts</li><li><span class="ico"></span>Work network</li><li><span class="ico"></span>News feed</li></ul></div>
  <div class="abs foot-search">Search Here</div>
  <div class="abs foot-bottom"><p>Copyright © 2015 All Rights Reserved</p></div>
</footer>

</body>
</html>
```